Corwick Roof Company need Flier for Department of Tillage

We need a 2 page flier for distributing to Military Contractors and Department of Tillage. We install residential solar and this will be used for military base housing and other gov. projects on the residential home communities. We need to show how large of a company we are and how we are able to work with the military //gov. projects. Attached is our website and other marketing info for your use. Thanks and good luck!

Target Market(s)

Military and Government Contractors //Department of Tillage

Industry/Entity Type

Solar Energy

Requirements
Must have
• Our Why - Statement included

```html
<!DOCTYPE html>
<html lang="en">
<head>
<meta charset="utf-8">
<title>Brightfield Energy – Rack Card</title>
<link href="https://fonts.googleapis.com/css2?family=Open+Sans:wght@400;600;700;800&display=swap" rel="stylesheet">
<style>
:root{
  --bg:#2b2c2e;
  --white:#ffffff;
  --blue:#2f97d6;
  --green:#8cc63f;
  --ink:#3a3d40;
  --muted:#7b8186;
  --panel:#f0f1f2;
  --bar-grey:#6b7075;
}
*{box-sizing:border-box;margin:0;padding:0}
html,body{width:1200px;height:900px;overflow:hidden}
body{background:var(--bg);font-family:"Open Sans",Arial,sans-serif;position:relative}
.card{position:absolute;top:45px;width:360px;height:810px;background:var(--white);overflow:hidden}
.card--front{left:210px}
.card--back{left:630px}
.bands{position:absolute;inset:0}
.brand{position:absolute;display:flex;align-items:center;gap:8px;white-space:nowrap}
.brand__dot{width:30px;height:30px;border-radius:50%;background:var(--blue);flex:none}
.brand__name{font-weight:700;font-size:19px;color:var(--blue);letter-spacing:.3px}
.card--front .brand{left:0;right:0;top:55px;justify-content:center}
.house-photo{position:absolute;left:0;top:130px;width:360px;height:300px;
  background:linear-gradient(160deg,#c9d6e2 0%,#8fa1b3 35%,#4a5563 65%,#3f5a38 100%)}
.front-copy{position:absolute;left:30px;right:24px;top:450px;color:var(--white)}
.headline{font-weight:800;font-size:22px;line-height:1.18}
.subline{font-size:16px;line-height:1.25;margin-top:10px}
.perks{list-style:none;margin-top:22px}
.perks li{display:flex;align-items:center;gap:10px;font-size:15px;margin-bottom:10px}
.perk-icon{width:26px;height:26px;border:1.5px solid var(--white);border-radius:50%;
  font-size:8px;display:flex;align-items:center;justify-content:center;font-weight:700;flex:none}
.phone-big{font-weight:800;font-size:23px;margin-top:14px}
.url-small{font-size:13px}
.rebate{position:absolute;left:30px;bottom:40px;color:var(--white)}
.rebate__lead{font-size:17px}
.rebate__offer{font-size:23px;font-weight:600}
/* back */
.card--back .brand{left:20px;top:34px;gap:6px}
.card--back .brand__dot{width:26px;height:26px}
.card--back .brand__name{font-size:14px}
.intro{position:absolute;left:20px;top:86px;width:172px;font-size:8.5px;line-height:1.45;color:var(--ink)}
.intro p+p{margin-top:8px}
.intro__lead{font-weight:700;color:var(--blue)}
.cost{position:absolute;left:208px;top:32px;width:134px}
.cost__title{font-weight:700;font-size:14px;line-height:1.15;color:var(--ink)}
.cost__bar{height:12px;margin-top:8px;font-size:7px;color:var(--white);padding-left:4px;line-height:12px}
.cost__bar--utility{background:var(--bar-grey);width:100%}
.cost__bar--solar{background:var(--green);width:70%;margin-top:3px}
.cost__years{display:flex;justify-content:space-between;font-size:7px;color:var(--muted);margin-top:4px}
.easy-label{position:absolute;left:0;right:0;top:218px;text-align:center;font-size:8px;color:var(--muted)}
.steps{position:absolute;left:14px;right:14px;top:236px;display:flex;justify-content:space-between}
.step{width:76px;text-align:center;font-size:7.5px;color:var(--ink)}
.step__icon{width:40px;height:40px;margin:0 auto 6px;border-radius:50%;border:2px solid var(--green);
  display:flex;align-items:center;justify-content:center}
.step__icon--blue{border-color:var(--blue)}
.reviews{position:absolute;left:28px;right:28px;top:340px;text-align:center}
.reviews__title{color:var(--green);font-weight:700;font-size:16px}
.review{font-size:9px;line-height:1.45;color:var(--ink);margin-top:14px}
.review__name{display:block;color:var(--green);font-weight:700;margin-top:3px}
.contact{position:absolute;left:0;right:0;bottom:48px;text-align:center;color:var(--white)}
.contact__label{font-size:15px}
.contact__phone{font-size:23px;font-weight:800}
.contact__address{font-size:10px;margin-top:2px}
.contact__url{font-size:18px;font-weight:700;margin-top:4px}
</style>
</head>
<body>

<section class="card card--front">
  <div class="brand"><span class="brand__dot"></span><span class="brand__name">Brightfield Energy</span></div>
  <div class="house-photo" role="img" aria-label="Photo of a modern white house with solar panels on the roof at dusk"></div>
  <svg class="bands" viewBox="0 0 360 810" width="360" height="810" aria-hidden="true">
    <polygon points="0,430 360,330 360,350 0,450" fill="#8cc63f"/>
    <polygon points="0,450 360,350 360,640 0,720" fill="#2f97d6"/>
    <polygon points="0,720 360,640 360,810 0,810" fill="#8cc63f"/>
  </svg>
  <div class="front-copy">
    <h1 class="headline">The Planet and your<br>Pocket will thank you.</h1>
    <p class="subline">Bringing the power of<br>the Sun to your Home</p>
    <ul class="perks">
      <li><span class="perk-icon">0%</span>Zero Upfront Cost</li>
      <li><span class="perk-icon">save</span>Lower Monthly Energy Cost</li>
    </ul>
    <p class="phone-big">(800) 555-0142</p>
    <p class="url-small">www.brightfieldenergy.com</p>
  </div>
  <div class="rebate">
    <p class="rebate__lead">Call today and Receive</p>
    <p class="rebate__offer">$500 Cash Rebate</p>
  </div>
</section>

<section class="card card--back">
  <svg class="bands" viewBox="0 0 360 810" width="360" height="810" aria-hidden="true">
    <polygon points="0,200 360,200 360,600 0,690" fill="#f0f1f2"/>
    <polygon points="0,690 360,590 360,810 0,810" fill="#8cc63f"/>
  </svg>
  <div class="brand"><span class="brand__dot"></span><span class="brand__name">Brightfield Energy</span></div>
  <div class="intro">
    <p><span class="intro__lead">Our Why:</span> we believe every military family deserves a home powered by clean, affordable energy, and our crews deliver it on base housing nationwide.</p>
    <p>Trusted by government contractors, we scale to whole communities with fast permits and no upfront cost.</p>
  </div>
  <div class="cost">
    <h2 class="cost__title">What Will My<br>Electricity Cost?</h2>
    <div class="cost__bar cost__bar--utility">Utility</div>
    <div class="cost__bar cost__bar--solar">Solar</div>
    <div class="cost__years"><span>Year 1</span><span>Year 10</span><span>Year 20</span></div>
  </div>
  <p class="easy-label">We Make It Easy</p>
  <div class="steps">
    <div class="step"><div class="step__icon step__icon--blue"><svg width="18" height="18" viewBox="0 0 18 18"><rect x="3" y="2" width="12" height="14" fill="none" stroke="#2f97d6" stroke-width="1.5"/></svg></div>Free Home Consult</div>
    <div class="step"><div class="step__icon step__icon--blue"><svg width="18" height="18" viewBox="0 0 18 18"><path d="M2 13 L9 4 L16 13 Z" fill="none" stroke="#2f97d6" stroke-width="1.5"/></svg></div>Custom System Design</div>
    <div class="step"><div class="step__icon"><svg width="18" height="18" viewBox="0 0 18 18"><path d="M3 9 L7 13 L15 5" fill="none" stroke="#8cc63f" stroke-width="2"/></svg></div>Fast Permit Approval</div>
    <div class="step"><div class="step__icon"><svg width="18" height="18" viewBox="0 0 18 18"><circle cx="9" cy="9" r="4" fill="none" stroke="#8cc63f" stroke-width="1.5"/></svg></div>Install and Save</div>
  </div>
  <div class="reviews">
    <h2 class="reviews__title">What People are Saying</h2>
    <p class="review">My husband and I decided to go solar after 3 of our neighbors did. After having it, I don't know why we waited so long!<span class="review__name">Dana R.</span></p>
    <p class="review">I had met with a few different companies and didn't care for their options. Brightfield had an option we liked and we have been very happy with our savings.<span class="review__name">Mark and Elise T.</span></p>
  </div>
  <div class="contact">
    <p class="contact__label">Contact Us:</p>
    <p class="contact__phone">(800) 555-0142</p>
    <p class="contact__address">118 Alder Rd. Suite 4-B, Fairhaven NJ 08000</p>
    <p class="contact__url">www.brightfieldenergy.com</p>
  </div>
</section>

</body>
</html>
```